Flyer-Design für Achtsamkeitscoaching
Zielgruppe
-Achtsamkeitscoaching - Stressbewältigung - Persönlichkeitsstärkung - Burnout Bewältigung
Aufgabenstellung
Faltflyer, 21 x 21cm, Titelseite: oberes Viertel soll 'härter' wirken - > anschließend in weichere Formen und Farbe übergehend, Grundfarbe = Pastell blaugrün, Logo + Akzente = Gold oder orange

```html
<!DOCTYPE html>
<html lang="de">
<head>
<meta charset="utf-8">
<title>Faltflyer Achtsamkeitscoaching</title>
<link href="https://fonts.googleapis.com/css2?family=Oswald:wght@500;600&family=Fira+Sans+Condensed:wght@400;600;700&family=Allura&family=Kaushan+Script&display=swap" rel="stylesheet">
<style>
:root{
  --stage:#c8c8c8;
  --teal:#3b7c87;
  --teal-deep:#2f6a75;
  --stone:#8d8b86;
  --stone-light:#b3b0aa;
  --rose:#e7a3b5;
  --lilac:#c8b3d8;
  --sea:#5e8d99;
  --sun:#f6ef9a;
  --gold:#d99a3a;
  --ink:#2a2a2e;
  --white:#ffffff;
  --paper-a:#eef0f6;
  --paper-b:#dfe8f2;
  --paper-c:#e9e2ef;
}
*{margin:0;padding:0;box-sizing:border-box}
html,body{width:1200px;height:2572px;overflow:hidden;background:var(--stage)}
body{position:relative;font-family:"Fira Sans Condensed",sans-serif}
.spread{position:absolute;left:100px;width:1000px;height:1080px;display:flex;box-shadow:0 14px 40px rgba(0,0,0,.18)}
.spread--outside{top:150px}
.spread--inside{top:1340px}
.panel{position:relative;width:500px;height:100%;overflow:hidden}
.band{position:absolute;left:0;right:0;height:18px;background:var(--teal);z-index:3}
.band--top{top:0}.band--bottom{bottom:0}
.fold{position:absolute;top:0;bottom:0;left:499px;width:2px;background:rgba(0,0,0,.08);z-index:4}

/* outside */
.sunset{position:absolute;inset:0;background:
  radial-gradient(ellipse 220px 120px at 50% 30%,var(--sun),rgba(246,239,154,0) 70%),
  linear-gradient(180deg,var(--lilac) 0%,#e3b2c8 22%,var(--rose) 32%,#9d8fb3 44%,#7d94b3 56%,var(--sea) 72%,var(--teal-deep) 100%)}
.panel--cover .sunset{background:
  radial-gradient(ellipse 200px 110px at 55% 34%,var(--sun),rgba(246,239,154,0) 70%),
  linear-gradient(180deg,var(--stone) 0%,var(--stone-light) 22%,#e2a9b6 30%,var(--rose) 36%,#a08db6 48%,#7f97b5 60%,var(--sea) 76%,var(--teal-deep) 100%)}
.back-intro{position:absolute;top:60px;left:44px;width:400px;color:var(--white);font-size:17px;line-height:1.35;opacity:.92}
.photo-circle{position:absolute;border-radius:50%;border:5px solid var(--white)}
.photo-dragonfly{top:210px;left:60px;width:220px;height:220px;background:radial-gradient(circle at 40% 40%,#e4ef7a,#9cc23c 55%,#5f8b2c)}
.power-title{position:absolute;top:520px;left:44px;color:var(--white);font-weight:700;font-size:24px;line-height:1.2}
.power-text{position:absolute;top:590px;left:44px;width:410px;color:var(--white);font-size:16.5px;line-height:1.38}
.power-text p+p{margin-top:10px}
.contact{position:absolute;top:880px;left:220px;color:var(--white)}
.contact .sign{font-family:"Allura",cursive;font-size:44px;line-height:1}
.contact .line{font-weight:700;font-size:18px;line-height:1.3}
.brand-mark{position:absolute;top:975px;left:44px;display:flex;align-items:center;gap:10px;color:var(--gold);font-weight:600;font-size:20px}
.brand-mark i{width:30px;height:30px;border-radius:50%;background:var(--gold);display:block}

.headline{position:absolute;top:50px;left:60px;color:var(--white);font-family:"Oswald",sans-serif;font-weight:600;font-size:74px;line-height:1.02;text-shadow:0 2px 6px rgba(0,0,0,.25)}
.headline span{display:block}
.headline span:nth-child(2){padding-left:90px}
.headline span:nth-child(3){padding-left:150px}
.claim{position:absolute;top:390px;left:50px;color:var(--white);font-family:"Kaushan Script",cursive;font-size:64px;transform:rotate(-10deg);transform-origin:left}
.claim-swash{position:absolute;top:445px;left:40px;width:430px;height:50px}
.service{position:absolute;top:500px;left:70px;color:var(--white);font-size:36px;letter-spacing:.5px;transform:rotate(-10deg);transform-origin:left}
.with-name{position:absolute;top:540px;left:250px;color:var(--white);font-family:"Allura",cursive;font-size:34px;transform:rotate(-10deg);transform-origin:left}
.qualities{position:absolute;top:640px;left:70px;color:var(--white);font-size:22px;line-height:1.15;list-style:none}
.qualities li{margin-bottom:14px}
.qualities li::before{content:"• "}
.qualities li span{display:block;padding-left:28px}
.certs{position:absolute;top:900px;left:70px;color:var(--white);font-weight:700;font-size:16px;line-height:1.15;list-style:none}
.certs li{display:flex;gap:6px;margin-bottom:10px}
.certs svg{width:16px;height:16px;flex:none;margin-top:2px}
.photo-portrait{top:690px;left:280px;width:260px;height:290px;border-radius:50% 0 0 50%;border:none;background:linear-gradient(160deg,#8c6a55,#c9a28a 45%,#6fc9c8 90%)}
.portrait-arc{position:absolute;top:680px;left:270px;width:250px;height:310px}

/* inside */
.paper{position:absolute;inset:0;background:
  radial-gradient(ellipse 300px 400px at 20% 70%,rgba(255,255,255,.55),transparent 70%),
  linear-gradient(160deg,var(--paper-c) 0%,var(--paper-a) 40%,var(--paper-b) 100%)}
.panel--right .paper{background:
  radial-gradient(ellipse 300px 380px at 70% 30%,rgba(255,255,255,.5),transparent 70%),
  linear-gradient(200deg,#d4e6f0 0%,var(--paper-a) 45%,var(--paper-c) 100%)}
.content{position:absolute;left:44px;right:36px;color:var(--ink);z-index:2}
.script-head{font-family:"Allura",cursive;font-size:40px;line-height:1.05;color:var(--ink)}
.brush{font-family:"Kaushan Script",cursive;color:var(--gold);font-size:72px;line-height:1}
.bullets{list-style:none;font-size:17px;line-height:1.3}
.bullets li{position:relative;padding-left:14px;margin-bottom:8px}
.bullets li::before{content:"•";position:absolute;left:0}
.bullets strong{font-weight:700}
.cta{font-family:"Kaushan Script",cursive;color:var(--gold);font-size:38px;line-height:1.1}
.cta-sub{font-size:18px}
</style>
</head>
<body>

<section class="spread spread--outside" aria-label="Außenseite">
  <article class="panel panel--back">
    <div class="sunset" role="img" aria-label="Foto: Meer bei Sonnenuntergang in Flieder, Rosa und Blaugrün"></div>
    <div class="band band--top"></div><div class="band band--bottom"></div>
    <p class="back-intro">In einem kurzen Vorgespräch schauen wir in Deine Lebensbereiche, damit Du einen IST-Stand für Dich erkennen kannst, an welchem du am Anfang Deiner Veränderung startest.</p>
    <div class="photo-circle photo-dragonfly" role="img" aria-label="Foto: Libelle vor grünem Hintergrund"></div>
    <h3 class="power-title">Krafttier Libelle:<br>ERLAUBNIS zum Richtungswechsel</h3>
    <div class="power-text">
      <p>Die Libelle fliegt in dein Leben und bringt Dir Mut, Liebe und Zuversicht. Sie begleitet Dich.</p>
      <p>Gehe langsam, achtsam und bewusst Deine nächsten Schritte. Dein Leben richtet sich neu aus. Gehe mit, lasse das Alte los und erlaube Dir einen Richtungswechsel. Nimm Dein Leben in die Hand und schaffe Platz für Neues. Jetzt bist Du bereit. Innerlich weißt Du schon, in welchen Bereichen Du einen wirklichen Richtungswechsel brauchst.</p>
      <p>Höre Dir selbst zu, so bewältigst Du ganz leicht die Hürden, die auf Deinem Weg auf Dich warten.</p>
    </div>
    <div class="contact">
      <div class="sign">Lena Marten</div>
      <div class="line">Mobil: 0171/2094638</div>
      <div class="line">lena.marten@webpost.de</div>
    </div>
    <div class="brand-mark"><i></i>Lena Marten</div>
  </article>

  <article class="panel panel--cover">
    <div class="sunset" role="img" aria-label="Foto: rissige Steinwand, übergehend in Meer bei Sonnenuntergang"></div>
    <div class="band band--top"></div><div class="band band--bottom"></div>
    <h1 class="headline"><span>Gestresst?</span><span>Erschöpft?</span><span>Genervt?</span></h1>
    <div class="claim">Ich helfe Dir!</div>
    <svg class="claim-swash" viewBox="0 0 430 50"><path d="M10 45 C140 20 280 5 420 2" stroke="#fff" stroke-width="3" fill="none" stroke-linecap="round"/></svg>
    <div class="service">Achtsamkeitscoaching</div>
    <div class="with-name">mit Lena Marten</div>
    <ul class="qualities">
      <li>Kompetent<span>&amp; erfahren</span></li>
      <li>Ganzheitlich<span>&amp; flexibel</span></li>
      <li>Persönlich<span>&amp; vertraulich</span></li>
    </ul>
    <ul class="certs">
      <li><svg viewBox="0 0 16 16"><path d="M2 9l4 4 8-10" stroke="#fff" stroke-width="2.5" fill="none"/></svg><span>Zertifizierte<br>Achtsamkeitstrainerin</span></li>
      <li><svg viewBox="0 0 16 16"><path d="M2 9l4 4 8-10" stroke="#fff" stroke-width="2.5" fill="none"/></svg><span>IHK-geprüfte<br>Stressmanagerin</span></li>
    </ul>
    <div class="photo-circle photo-portrait" role="img" aria-label="Porträtfoto der Coachin"></div>
    <svg class="portrait-arc" viewBox="0 0 250 310"><path d="M200 5 A150 150 0 0 0 200 305" stroke="#fff" stroke-width="4" fill="none"/></svg>
  </article>
  <div class="fold"></div>
</section>

<section class="spread spread--inside" aria-label="Innenseite">
  <article class="panel panel--left">
    <div class="paper" role="img" aria-label="Hintergrund: zarte skelettierte Blätter in Pastell"></div>
    <div class="band band--top"></div><div class="band band--bottom"></div>
    <div class="content" style="top:50px">
      <h2 class="script-head">Ist mein Achtsamkeits-<br>coaching für Dich geeignet?</h2>
      <div class="brush" style="margin:22px 0 10px">Yes!</div>
      <ul class="bullets">
        <li>Wenn du raus willst, aus deinem privaten und/ oder beruflichen Stress-Hamsterrad</li>
        <li>Wenn du dich müde, gereizt, verspannt, unruhig, wenig belastbar und unkonzentriert fühlst</li>
        <li>Wenn du das Gefühl hast, in dieser schnelllebigen Zeit selbst zu kurz zu kommen</li>
        <li>Wenn du Dinge nicht nur verstehen, sondern auch umsetzen willst</li>
        <li>Wenn du nach Selbstvertrauen, Klarheit und innerer Ruhe strebst und bereit bist deine Komfortzone dafür zu verlassen</li>
        <li><strong>Wenn Du wieder Du selbst werden möchtest und Dich wieder fühlen willst!</strong></li>
      </ul>
      <div class="brush" style="margin:60px 0 10px">No!</div>
      <ul class="bullets">
        <li>Wenn du nur einen kurzen Motivationskick suchst und nicht bereit bist deine Verhaltensmuster zu hinterfragen.</li>
        <li>Wenn du keine Zeit und kein Geld in dich investieren möchtest.</li>
      </ul>
    </div>
  </article>

  <article class="panel panel--right">
    <div class="paper" role="img" aria-label="Hintergrund: zarte skelettierte Blätter in Pastell"></div>
    <div class="band band--top"></div><div class="band band--bottom"></div>
    <div class="content" style="top:60px">
      <h2 class="script-head" style="margin-bottom:20px">Vorteile deines Coachings:</h2>
      <ul class="bullets">
        <li>Du wirst individuell und persönlich betreut.</li>
        <li>Herzlich und offen – ich begleite dich, ohne dich zu bewerten.</li>
        <li>Schneller Einstieg möglich.</li>
        <li>Keine Vorkenntnisse notwendig.</li>
        <li>Ganzheitlich – ich bringe dich nicht nur auf den Weg in die Achtsamkeit, sondern betrachte Deine Symptome auch in größeren Zusammenhängen.</li>
        <li>Planbar – das Coaching findet einmal pro Woche im Zeitraum von acht Wochen statt – nimm Dir die Zeit!</li>
      </ul>
      <ul class="bullets" style="margin-top:24px">
        <li>Zielgruppe: ALLE! – mein Coaching ist für Dich geeignet, wenn du dir sagst: <strong>„Ich will es – jetzt!“</strong></li>
        <li>Das besondere Geschenk für deine(n) Partnerin/ Partner – und die Krönung ist, wenn ihr es gemeinsam angeht. Liebe beruht auf Gegenseitigkeit.</li>
        <li>Ideal für Paare – es kann nur noch besser werden</li>
      </ul>
      <ul class="bullets" style="margin-top:24px">
        <li><strong>Ein Wort zu Vorurteilen:</strong><br>Nein, es sind keine Hokuspokus-Stunden oder spirituelle Beweihräucherungen. Die Lehre der Achtsamkeit beruht auf langjährig erprobten und wissenschaftlich fundamentierten Erkenntnissen und ist längst in der modernen Arbeitswelt fest integriert.</li>
      </ul>
      <div class="cta" style="margin-top:30px">Nimm jetzt Kontakt auf!</div>
      <div class="cta-sub">Die Anmeldung ist ganz einfach …</div>
    </div>
  </article>
  <div class="fold"></div>
</section>

</body>
</html>
```